Business Card Design Project

We require a business card template to cover basic contact information - our company logo, names of employees, title, mobile and email.

Target Market(s)

Corporate

Industry/Entity Type

Business

Font styles to use
Sans Serif

Requirements
Nice to have
• Thinking it would be great just to have the logo taking up approximately half the space (so it goes as far across the top of the card as possible) and then contact details in the lower half of the card. Keen just to use only the two colours in the logo, on a white background.
Should not have
• No fussy drawings

```html
<!DOCTYPE html>
<html lang="en">
<head>
<meta charset="utf-8">
<title>Tidewell Developments – Business Card</title>
<link rel="stylesheet" href="https://fonts.googleapis.com/css2?family=Jost:wght@400&display=swap">
<style>
  :root {
    --backdrop: #e4e9e9;
    --card: #ffffff;
    --teal: #4fcfb6;
    --blue: #2f6fe0;
    --white: #ffffff;
  }
  * { margin: 0; padding: 0; box-sizing: border-box; }
  html, body {
    width: 1200px;
    height: 617px;
    overflow: hidden;
    background: var(--backdrop);
    font-family: "Jost", "Futura", sans-serif;
  }
  .business-card {
    position: absolute;
    left: 240px;
    top: 88px;
    width: 720px;
    height: 441px;
    background: var(--card);
    box-shadow: 4px 5px 8px rgba(0, 0, 0, 0.25);
  }
  .brand-name {
    position: absolute;
    left: 0;
    right: 0;
    top: 58px;
    text-align: center;
    color: var(--teal);
    font-weight: 400;
    line-height: 1;
  }
  .brand-name .brand-main {
    display: block;
    font-size: 112px;
    letter-spacing: -2px;
  }
  .brand-name .brand-sub {
    display: block;
    font-size: 30px;
    margin-top: 2px;
    padding-left: 250px;
  }
  .contact-band {
    position: absolute;
    left: 0;
    right: 0;
    top: 278px;
    height: 106px;
    background: var(--blue);
    color: var(--white);
  }
  .person {
    position: absolute;
    left: 56px;
    top: 22px;
  }
  .person-name { font-size: 22px; line-height: 1.2; }
  .person-title { font-size: 19px; line-height: 1.2; opacity: 0.9; }
  .contact-list {
    position: absolute;
    left: 280px;
    top: 18px;
    list-style: none;
  }
  .contact-item {
    display: flex;
    align-items: center;
    height: 36px;
    font-size: 20px;
  }
  .contact-icon {
    width: 26px;
    height: 26px;
    margin-right: 20px;
    flex: none;
  }
</style>
</head>
<body>
  <main class="business-card">
    <h1 class="brand-name">
      <span class="brand-main">Tidewell</span>
      <span class="brand-sub">developments</span>
    </h1>

    <section class="contact-band">
      <div class="person">
        <p class="person-name">John Doe Smith</p>
        <p class="person-title">CEO</p>
      </div>

      <ul class="contact-list">
        <li class="contact-item">
          <svg class="contact-icon" viewBox="0 0 26 26" aria-hidden="true">
            <circle cx="13" cy="13" r="13" fill="#ffffff"/>
            <rect x="9" y="6" width="8" height="14" rx="1.5" fill="none" stroke="#2f6fe0" stroke-width="1.6"/>
            <circle cx="13" cy="17.5" r="0.9" fill="#2f6fe0"/>
          </svg>
          <span class="contact-text">0400 182 736</span>
        </li>
        <li class="contact-item">
          <svg class="contact-icon" viewBox="0 0 26 26" aria-hidden="true">
            <circle cx="13" cy="13" r="13" fill="#ffffff"/>
            <rect x="6.5" y="8.5" width="13" height="9" fill="none" stroke="#2f6fe0" stroke-width="1.5"/>
            <path d="M6.5 8.5 L13 13.5 L19.5 8.5" fill="none" stroke="#2f6fe0" stroke-width="1.5"/>
          </svg>
          <span class="contact-text">hello@tidewelldevelopments.com</span>
        </li>
      </ul>
    </section>
  </main>
</body>
</html>
```